Bref créative
Valtoria
business card, letterhead and envelope
Professional
Dale Morrow
CEO
4718 Piney Brook Rd
Ashbury, AZ 86021
dale@valtnet.us
www.valtnet.us

```html
<!DOCTYPE html>
<html lang="en">
<head>
<meta charset="utf-8">
<title>Valtoria Stationery</title>
<link href="https://fonts.googleapis.com/css2?family=Michroma&family=Open+Sans:wght@400;600;700&display=swap" rel="stylesheet">
<style>
  :root {
    --stage: #2b2b2d;
    --paper: #ffffff;
    --paper-shade: #eceff2;
    --blue-deep: #0a5fa8;
    --blue-mid: #1a86d6;
    --blue-light: #5cb4f0;
    --ink: #2d2f33;
    --on-blue: #e9f5ff;
  }
  html, body { margin: 0; padding: 0; width: 1200px; height: 961px; overflow: hidden; background: var(--stage); }
  body { position: relative; font-family: "Open Sans", Arial, sans-serif; color: var(--ink); }
  .piece { position: absolute; box-shadow: 0 6px 18px rgba(0,0,0,.45); overflow: hidden; }
  .wordmark {
    font-family: "Michroma", "Open Sans", sans-serif;
    color: var(--ink); letter-spacing: .12em; display: flex; align-items: center; gap: .5em; white-space: nowrap;
  }
  .wordmark .mark { width: .7em; height: .7em; background: var(--blue-mid); display: inline-block; }

  /* Letterhead */
  .letterhead { left: 190px; top: 21px; width: 680px; height: 894px; background: var(--paper); }
  .letterhead .wordmark { position: absolute; left: 52px; top: 52px; font-size: 30px; }
  .letterhead .rule { position: absolute; left: 0; right: 0; top: 114px; height: 2px; background: var(--paper-shade); }
  .letterhead .footer {
    position: absolute; left: 0; right: 0; bottom: 0; height: 143px;
    background: linear-gradient(180deg, var(--blue-light), var(--blue-mid) 45%, var(--blue-deep));
    color: var(--on-blue); font-size: 9px; text-align: center;
  }
  .letterhead .footer p { margin: 0; }
  .letterhead .footer .addr { margin-top: 62px; }
  .letterhead .footer .lines { margin-top: 10px; word-spacing: 12px; }
  .letterhead .footer .web { margin-top: 14px; font-weight: 600; }

  /* Business card front */
  .card-front { left: 57px; top: 338px; width: 283px; height: 138px; background: var(--paper); }
  .card-front .wordmark { position: absolute; left: 16px; top: 14px; font-size: 14px; }
  .card-front .band {
    position: absolute; left: 0; right: 0; top: 50px; bottom: 0;
    background: linear-gradient(180deg, var(--blue-mid), var(--blue-deep));
    color: var(--on-blue); font-size: 7px; line-height: 1.4;
  }
  .card-front .name { position: absolute; left: 16px; top: 10px; font-size: 10px; font-weight: 700; }
  .card-front .role { position: absolute; left: 16px; top: 25px; font-size: 7px; }
  .card-front .contact { position: absolute; left: 158px; top: 7px; margin: 0; }

  /* Business card back */
  .card-back {
    left: 57px; top: 540px; width: 283px; height: 157px;
    background: linear-gradient(160deg, var(--blue-light), var(--blue-mid) 40%, var(--blue-deep));
  }
  .card-back .web { position: absolute; left: 20px; top: 14px; font-size: 8px; color: var(--on-blue); }
  .card-back .wordmark { position: absolute; left: 20px; top: 104px; font-size: 17px; color: var(--paper); }
  .card-back .wordmark .mark { background: var(--paper); }

  /* Envelope */
  .envelope { left: 390px; top: 385px; width: 761px; height: 408px; background: var(--paper); }
  .envelope .flap {
    position: absolute; left: 0; right: 0; top: 0; height: 70px;
    background: linear-gradient(90deg, var(--blue-light), var(--blue-mid) 50%, var(--blue-deep));
  }
  .envelope .side {
    position: absolute; right: 0; top: 70px; width: 90px; bottom: 30px;
    background: linear-gradient(90deg, rgba(26,134,214,0), rgba(26,134,214,.5));
  }
  .envelope .wordmark { position: absolute; left: 52px; top: 105px; font-size: 26px; }
  .envelope .base {
    position: absolute; left: 0; right: 0; bottom: 0; height: 30px;
    background: linear-gradient(180deg, var(--blue-mid), var(--blue-deep));
    color: var(--on-blue); font-size: 8px; line-height: 30px; padding-left: 52px;
  }
</style>
</head>
<body>

<section class="piece letterhead" aria-label="Letterhead">
  <div class="wordmark"><span class="mark"></span>VALTORIA</div>
  <div class="rule"></div>
  <footer class="footer">
    <p class="addr">4718 Piney Brook Rd, Ashbury, AZ 86021</p>
    <p class="lines">Tel&nbsp;928.555.0142 Fax&nbsp;928.555.0143 Cell&nbsp;928.555.0144 dale@valtnet.us</p>
    <p class="web">www.valtnet.us</p>
  </footer>
</section>

<section class="piece card-front" aria-label="Business card front">
  <div class="wordmark"><span class="mark"></span>VALTORIA</div>
  <div class="band">
    <div class="name">Dale Morrow</div>
    <div class="role">CEO</div>
    <p class="contact">4718 Piney Brook Rd<br>Ashbury, AZ 86021<br>Tel 928.555.0142<br>Fax 928.555.0143<br>Cell 928.555.0144<br>dale@valtnet.us</p>
  </div>
</section>

<section class="piece card-back" aria-label="Business card back">
  <div class="web">www.valtnet.us</div>
  <div class="wordmark"><span class="mark"></span>VALTORIA</div>
</section>

<section class="piece envelope" aria-label="Envelope">
  <div class="flap"></div>
  <div class="side"></div>
  <div class="wordmark"><span class="mark"></span>VALTORIA</div>
  <div class="base">4718 Piney Brook Rd, Ashbury, AZ 86021</div>
</section>

</body>
</html>
```